Email Signature

We would like to have an email Signature designed.
We have an idea, and a logo that we would like to be make more professional in design and look.

```html
<!DOCTYPE html>
<html lang="en">
<head>
<meta charset="utf-8">
<title>Email Signature – Kestrel Consulting</title>
<link rel="stylesheet" href="https://fonts.googleapis.com/css2?family=Arimo:wght@400;700&display=swap">
<style>
  :root {
    --page: #ffffff;
    --card: #ffffff;
    --ink: #111111;
    --brand-blue: #0a72b9;
    --brand-orange: #ef5a32;
    --panel-grey: #e8e8ea;
    --shadow: rgba(0, 0, 0, 0.45);
  }
  * { margin: 0; padding: 0; box-sizing: border-box; }
  html, body {
    width: 1200px;
    height: 446px;
    overflow: hidden;
    background: var(--page);
    font-family: "Arimo", Arial, sans-serif;
    color: var(--ink);
  }
  .signature {
    position: absolute;
    left: 48px;
    top: 80px;
    width: 1104px;
    height: 298px;
    background: var(--card);
    box-shadow: 0 2px 7px var(--shadow);
    overflow: hidden;
  }
  .signature__bands {
    position: absolute;
    inset: 0;
    width: 100%;
    height: 100%;
  }
  .band--panel { fill: var(--panel-grey); }
  .band--blue { fill: var(--brand-blue); }
  .band--orange { fill: var(--brand-orange); }
  .contact {
    position: absolute;
    left: 63px;
    top: 22px;
  }
  .contact__name {
    font-weight: 700;
    font-size: 34px;
    letter-spacing: -0.6px;
    line-height: 1;
    transform: scaleX(0.92);
    transform-origin: left;
  }
  .contact__role {
    font-size: 16px;
    margin-top: 4px;
  }
  .contact__lines {
    margin-top: 17px;
    font-size: 15px;
    line-height: 22px;
  }
  .contact__footer {
    position: absolute;
    left: 63px;
    top: 221px;
    font-size: 15px;
    line-height: 21px;
  }
  .brand {
    position: absolute;
    left: 770px;
    top: 148px;
    width: 320px;
    text-align: center;
    color: var(--brand-blue);
    font-weight: 700;
    line-height: 1;
  }
  .brand__name { font-size: 50px; letter-spacing: 1px; }
  .brand__tag { font-size: 30px; letter-spacing: 3px; margin-top: 4px; }
</style>
</head>
<body>
  <div class="signature">
    <svg class="signature__bands" viewBox="0 0 1104 298" preserveAspectRatio="none" aria-hidden="true">
      <polygon class="band--panel" points="880,0 1104,0 1104,298 740,298"/>
      <polygon class="band--blue" points="850,0 872,0 732,298 710,298"/>
      <polygon class="band--orange" points="826,0 836,0 696,298 686,298"/>
    </svg>

    <div class="contact">
      <h1 class="contact__name">Sam Whitfield</h1>
      <p class="contact__role">Client Relations</p>
      <p class="contact__lines">
        Mobile: +61400 555 018<br>
        Email: hello@kestrelconsult.com
      </p>
    </div>

    <p class="contact__footer">
      add : 123-xxx ,contry<br>
      www.websitename.com
    </p>

    <div class="brand">
      <div class="brand__name">KESTREL</div>
      <div class="brand__tag">consulting</div>
    </div>
  </div>
</body>
</html>
```